Beyond The Ledger Double Sided DL Flyer

We need a double sided flyer that we provide to a Real Estate agent for leeds. It should provide our basic services as well as a modern look and feel. The brochure should incorporate our Brand colors and have a graphic that centres around money and property. I have included a couple of pictures that we like (but have not yet purchased from PIXVAULT) as an indication of the type of picture we like.

WE need to also show the Beyond The Ledger brand and have our Phone / address's and email details.

Target Market(s)

Realestate clients (Property Investors)

Industry/Entity Type

Financial Planning

Requirements
Must have
• Picture on Front (maybe the logo on back)
• Please incorporate existing logo colours.

```html
<!DOCTYPE html>
<html lang="en">
<head>
<meta charset="utf-8">
<title>Beyond The Ledger – DL Flyer</title>
<link href="https://fonts.googleapis.com/css2?family=Raleway:wght@400;500;600;700;800&display=swap" rel="stylesheet">
<style>
:root{
  --green:#7cc12e;
  --green-light:#8fd03a;
  --charcoal:#2a2a2a;
  --charcoal-deep:#1f1f1f;
  --ink:#1e1e1e;
  --gold:#c8903e;
  --silver:#d9d9d9;
  --stage:#e4e4e4;
  --white:#ffffff;
}
*{margin:0;padding:0;box-sizing:border-box}
html,body{width:1200px;height:1200px;overflow:hidden}
body{background:var(--stage);font-family:"Raleway",Arial,sans-serif;position:relative;color:var(--ink)}
.panel{position:absolute;top:54px;width:484px;height:1028px;background:var(--white);overflow:hidden}
.panel--front{left:82px}
.panel--back{left:634px}
.panel__art{position:absolute;inset:0;width:484px;height:1028px}
.label{position:absolute;top:1118px;width:484px;text-align:center;font-size:27px;color:#3a3a3a;font-weight:400;letter-spacing:.5px}
.label--front{left:82px}
.label--back{left:634px}

.brand{position:absolute;left:0;width:484px;display:flex;align-items:center;justify-content:center;gap:10px}
.brand__mark{width:14px;height:14px;background:var(--green)}
.brand__name{font-weight:800;color:var(--charcoal);letter-spacing:.3px}
.panel--front .brand{top:912px}
.panel--front .brand__name{font-size:34px}
.panel--back .brand{top:806px}
.panel--back .brand__name{font-size:27px}

.call{position:absolute;left:0;top:978px;width:484px;height:40px;background:var(--charcoal);color:var(--white);font-size:29px;font-weight:500;display:flex;align-items:center;justify-content:center;gap:8px}
.call__num{color:var(--green);font-weight:700}
.call-strip{position:absolute;left:0;top:1018px;width:484px;height:10px;background:var(--green)}

.intro{position:absolute;left:14px;top:48px;width:456px;text-align:center;font-size:17px;line-height:23px;font-weight:500;color:#222}
.pill{position:absolute;left:19px;top:144px;width:445px;height:44px;border-radius:12px;background:var(--green);color:var(--white);font-weight:700;font-size:17px;line-height:20px;text-align:center;padding-top:3px;box-shadow:0 6px 8px -4px rgba(0,0,0,.35)}

.services{list-style:none;position:absolute;left:0;top:0}
.service{position:absolute;left:54px;width:420px;height:72px;display:flex;align-items:center}
.service__icon{width:72px;height:72px;flex:none}
.service__text{margin-left:15px;font-size:18.5px;line-height:21px;font-weight:700}
.service__lead{color:var(--green);display:block}
.service__tail{color:var(--ink);display:block}

.contact{position:absolute;left:0;width:484px;text-align:center;font-size:17px;font-weight:500;color:#222;display:flex;justify-content:center;align-items:center;gap:8px}
.contact svg{width:16px;height:16px;flex:none}
.contact--note{color:var(--green);gap:0}
</style>
</head>
<body>

<!-- FRONT -->
<section class="panel panel--front">
  <svg class="panel__art" viewBox="0 0 484 1028" aria-hidden="false">
    <defs>
      <linearGradient id="photoTone" x1="0" y1="0" x2="1" y2="1">
        <stop offset="0" stop-color="#4f8f32"/>
        <stop offset=".55" stop-color="#6aa63f"/>
        <stop offset="1" stop-color="#8a7a5e"/>
      </linearGradient>
      <linearGradient id="silverFade" x1="0" y1="0" x2="1" y2="0">
        <stop offset="0" stop-color="#bdbdbd"/><stop offset=".5" stop-color="#f2f2f2"/><stop offset="1" stop-color="#bdbdbd"/>
      </linearGradient>
    </defs>
    <rect width="484" height="1028" fill="var(--charcoal)"/>
    <path d="M0,72 Q242,8 484,84 L484,140 L0,140 Z" fill="var(--gold)"/>
    <path d="M0,545 L238,622 L484,545 L484,560 L238,640 L0,560 Z" fill="url(#silverFade)"/>
    <g role="img" aria-label="Photo: hand watering a seedling growing from a jar of coins beside a small house model and coin stacks">
      <path d="M0,78 Q242,16 484,90 L484,530 L238,610 L0,530 Z" fill="url(#photoTone)"/>
    </g>
    <path d="M0,560 L238,640 L140,660 L0,680 Z" fill="var(--green)"/>
    <path d="M0,560 L238,640 L484,720 L484,880 L0,680 Z" fill="var(--green)"/>
    <path d="M0,680 L484,880 L484,1028 L0,1028 Z" fill="var(--charcoal-deep)"/>
    <path d="M0,834 L154,738 L484,870 L484,1028 L0,1028 Z" fill="var(--green)"/>
    <path d="M0,842 L154,746 L484,878 L484,1028 L0,1028 Z" fill="var(--white)"/>
  </svg>
  <div class="brand"><span class="brand__mark"></span><span class="brand__name">Beyond The Ledger</span></div>
  <div class="call">CALL US : <span class="call__num">(02) 5550 1842</span></div>
  <div class="call-strip"></div>
</section>

<!-- BACK -->
<section class="panel panel--back">
  <svg class="panel__art" viewBox="0 0 484 1028" aria-hidden="true">
    <rect width="484" height="1028" fill="var(--white)"/>
    <path d="M0,0 L484,0 L484,58 Q242,-6 0,58 Z" fill="var(--charcoal)"/>
    <path d="M0,58 Q242,-6 484,58 L484,54 Q242,2 0,54 Z" fill="var(--gold)"/>
    <path d="M0,620 L484,600 L484,1028 L0,1028 Z" fill="var(--charcoal-deep)"/>
    <path d="M0,620 L484,740 L484,810 L0,690 Z" fill="var(--green)"/>
    <path d="M0,620 L240,680 L484,620 L484,740 Z" fill="var(--green)"/>
    <path d="M0,780 L166,740 L484,804 L484,1028 L0,1028 Z" fill="var(--green)"/>
    <path d="M0,786 L166,746 L484,810 L484,1028 L0,1028 Z" fill="var(--white)"/>
  </svg>

  <p class="intro">We are a professional accounting firm and require a double sided DL Flyer that can be given out by a&nbsp; Real-estate Agent / Property Conveyancer to prospective clients marketing our services.</p>
  <div class="pill">ACCOUNTANTS AND FINANCIAL ADVISORS<br>WHO SPECIALISE IN</div>

  <ul class="services">
    <li class="service" style="top:204px">
      <svg class="service__icon" viewBox="0 0 72 72"><circle cx="36" cy="36" r="34" fill="none" stroke="#222" stroke-width="1.5" stroke-dasharray="4 3"/><circle cx="36" cy="40" r="17" fill="var(--green)"/><path d="M30,20 h12 l-3,6 h-6 Z" fill="var(--green)"/><text x="36" y="47" text-anchor="middle" font-family="Raleway,sans-serif" font-weight="700" font-size="20" fill="#fff">$</text></svg>
      <span class="service__text"><span class="service__lead">Negative Gearing &amp;</span><span class="service__tail">Investment Properties</span></span>
    </li>
    <li class="service" style="top:290px">
      <svg class="service__icon" viewBox="0 0 72 72"><circle cx="36" cy="36" r="34" fill="none" stroke="#222" stroke-width="1.5" stroke-dasharray="4 3"/><path d="M38,16 l14,12 h-4 v10 h-20 v-10 h-4 Z" fill="var(--green)"/><path d="M14,44 h8 l8,4 h14 l10,-6 v6 l-12,8 h-14 l-6,-3 h-8 Z" fill="var(--green)"/></svg>
      <span class="service__text"><span class="service__lead">Property &amp; Capital Gains</span><span class="service__tail">Tax Minimisation</span></span>
    </li>
    <li class="service" style="top:375px">
      <svg class="service__icon" viewBox="0 0 72 72"><circle cx="36" cy="36" r="34" fill="none" stroke="#222" stroke-width="1.5" stroke-dasharray="4 3"/><ellipse cx="28" cy="44" rx="11" ry="4" fill="var(--green)"/><ellipse cx="28" cy="38" rx="11" ry="4" fill="var(--green)" stroke="#fff"/><ellipse cx="46" cy="40" rx="11" ry="4" fill="var(--green)"/><ellipse cx="46" cy="34" rx="11" ry="4" fill="var(--green)" stroke="#fff"/><ellipse cx="46" cy="28" rx="11" ry="4" fill="var(--green)" stroke="#fff"/></svg>
      <span class="service__text"><span class="service__lead">Self-Managed</span><span class="service__tail">Superannuation Funds (SMSF)</span></span>
    </li>
    <li class="service" style="top:462px">
      <svg class="service__icon" viewBox="0 0 72 72"><circle cx="36" cy="36" r="34" fill="none" stroke="#222" stroke-width="1.5" stroke-dasharray="4 3"/><rect x="30" y="19" width="12" height="7" rx="2" fill="none" stroke="var(--green)" stroke-width="3"/><rect x="16" y="25" width="40" height="28" rx="3" fill="var(--green)"/><rect x="33" y="35" width="6" height="5" fill="#fff"/></svg>
      <span class="service__text"><span class="service__lead">Small Business &amp;</span><span class="service__tail">Personal Taxation</span></span>
    </li>
    <li class="service" style="top:547px">
      <svg class="service__icon" viewBox="0 0 72 72"><circle cx="36" cy="36" r="34" fill="none" stroke="#222" stroke-width="1.5" stroke-dasharray="4 3"/><path d="M36,18 L56,52 H16 Z" fill="none" stroke="var(--green)" stroke-width="4" stroke-linejoin="round"/><rect x="34" y="30" width="4" height="12" fill="var(--green)"/><circle cx="36" cy="46" r="2.2" fill="var(--green)"/></svg>
      <span class="service__text"><span class="service__lead">Investment Advice &amp;</span><span class="service__tail">Risk Insurances</span></span>
    </li>
  </ul>

  <div class="brand"><span class="brand__mark"></span><span class="brand__name">Beyond The Ledger</span></div>

  <p class="contact" style="top:868px"><svg viewBox="0 0 16 16"><path d="M8,1 a5,5 0 0 1 5,5 c0,4 -5,9 -5,9 s-5,-5 -5,-9 a5,5 0 0 1 5,-5 Z" fill="var(--green)"/><circle cx="8" cy="6" r="2" fill="#fff"/></svg>7 / 118 Harbour View Rd Westbay NSW 2251</p>
  <p class="contact" style="top:897px"><svg viewBox="0 0 16 16"><path d="M8,1 a5,5 0 0 1 5,5 c0,4 -5,9 -5,9 s-5,-5 -5,-9 a5,5 0 0 1 5,-5 Z" fill="var(--green)"/><circle cx="8" cy="6" r="2" fill="#fff"/></svg>2 / 31 Kingfisher St Lakeside NSW 2264</p>
  <p class="contact contact--note" style="top:921px">(By Appointment)</p>
  <p class="contact" style="top:947px"><svg viewBox="0 0 16 16"><circle cx="8" cy="8" r="7.5" fill="var(--green)"/><rect x="4" y="5" width="8" height="6" rx="1" fill="#fff"/><path d="M4,5.5 L8,8.5 L12,5.5" fill="none" stroke="var(--green)" stroke-width="1"/></svg>hello@beyondtheledger.com.au</p>

  <div class="call">CALL US : <span class="call__num">(02) 5550 1842</span></div>
  <div class="call-strip"></div>
</section>

<p class="label label--front">FRONT</p>
<p class="label label--back">BACK</p>

</body>
</html>
```